Attorney business card for two offices

Looking for a new business card design that can list both of my offices, one in Houston and one in West Texas. Want something masculine, easy to read, and conservative yet somewhat modern. Our current card has used a nautical star on it for years, but I am not necessarily attached to that. Also, a lot of our forms use dark green and orange. Second office address is P.O. Box 518, Marathon, Texas 79617

```html
<!DOCTYPE html>
<html lang="en">
<head>
<meta charset="utf-8">
<title>The Whitaker Law Firm – Business Card</title>
<link href="https://fonts.googleapis.com/css2?family=Libre+Franklin:wght@400;500;600&display=swap" rel="stylesheet">
<style>
  :root {
    --backdrop: #d4d4d4;
    --paper: #ffffff;
    --firm-green: #3a664b;
    --accent-orange: #f9a71c;
    --ink-light: #ffffff;
  }
  * { margin: 0; padding: 0; box-sizing: border-box; }
  html, body {
    width: 1200px; height: 795px; overflow: hidden;
    background: var(--backdrop);
    font-family: "Libre Franklin", Arial, sans-serif;
  }
  .card {
    position: absolute; left: 38px; top: 72px;
    width: 1124px; height: 651px;
    display: flex;
  }
  .brand-panel {
    width: 467px; height: 100%;
    background: var(--paper);
    position: relative;
  }
  .brand-mark {
    position: absolute; left: 50%; top: 272px;
    width: 22px; height: 22px; margin-left: -11px;
    border-radius: 50%;
    background: var(--firm-green);
  }
  .firm-name {
    position: absolute; left: 0; right: 0; top: 336px;
    text-align: center;
    color: var(--firm-green);
    font-weight: 600; font-size: 23px; letter-spacing: 1.6px;
    text-transform: uppercase;
  }
  .accent-band { width: 48px; height: 100%; background: var(--accent-orange); }
  .contact-panel {
    flex: 1; height: 100%;
    background: var(--firm-green);
    color: var(--ink-light);
    position: relative;
    padding-left: 84px;
    text-transform: uppercase;
  }
  .contact-panel > * { position: absolute; left: 84px; white-space: nowrap; }
  .attorney-name { top: 95px; font-size: 26px; font-weight: 500; letter-spacing: 2px; }
  .attorney-title { top: 139px; font-size: 23px; font-weight: 400; letter-spacing: 2px; }
  .office-label { color: var(--accent-orange); font-size: 20px; font-weight: 600; letter-spacing: 1px; }
  .office-line, .contact-line { font-size: 20px; letter-spacing: 1.4px; font-weight: 400; }
  .office-houston { top: 256px; }
  .houston-street { top: 292px; }
  .houston-city { top: 329px; }
  .office-west { top: 403px; }
  .west-address { top: 439px; text-transform: none; font-variant: small-caps; }
  .contact-phone { top: 497px; }
  .contact-email { top: 534px; }
  .contact-key { color: var(--accent-orange); font-weight: 600; }
  .contact-gap { display: inline-block; width: 22px; }
</style>
</head>
<body>
  <div class="card">
    <section class="brand-panel">
      <span class="brand-mark" aria-hidden="true"></span>
      <h1 class="firm-name">The Whitaker Law Firm, P.C.</h1>
    </section>
    <div class="accent-band"></div>
    <section class="contact-panel">
      <h2 class="attorney-name">Daniel R. Whitaker, Sr.</h2>
      <p class="attorney-title">Attorney at Law</p>

      <h3 class="office-label office-houston">Houston</h3>
      <p class="office-line houston-street">4410 Katy Freeway, Suite 208</p>
      <p class="office-line houston-city">Houston, Texas 77055</p>

      <h3 class="office-label office-west">West Texas</h3>
      <p class="office-line west-address">P.O. Box 518, Marathon, Texas 79617</p>

      <p class="contact-line contact-phone"><span class="contact-key">P:</span> (713) 555-0142<span class="contact-gap"></span><span class="contact-key">F:</span> (832) 555-0187</p>
      <p class="contact-line contact-email"><span class="contact-key">E:</span> daniel@whitakertxlaw.com</p>
    </section>
  </div>
</body>
</html>
```